Financial Dashboard UI design

We are building a financial dashboard for business management teams, and would like a futuristic and sophisticated design (light and dark themes).

There are a total of 3 screens (attached images: nemo1, nemo2, nemo3).
nemo1 image is comprised of 6 scorecards (attached image: scorecard)
This will also need a design.

So, I'm expecting 4 UI designs in total.

I've added some example UI for inspiration. (sample1 , sample2, sample3, sample4).

Thanks

```html
<!DOCTYPE html>
<html lang="en">
<head>
<meta charset="utf-8">
<title>Budget Scorecards</title>
<link rel="stylesheet" href="https://fonts.googleapis.com/css2?family=Oswald:wght@500;600&family=Poppins:wght@400;500;600&display=swap">
<style>
:root{
  --page:#16142c;
  --card:#232141;
  --card-head:#2a2849;
  --card-foot:#2c2a4c;
  --ghost:rgba(255,255,255,.035);
  --chip:#3a385c;
  --chip-line:#4a486e;
  --text:#ffffff;
  --muted:#c9c8dc;
  --accent:#f4e600;
  --bar-empty:#ffffff;
  --bar-unpaid:#88a9d5;
  --bar-paid:#4270a9;
  --up:#1db530;
  --down:#ee1c1c;
  --warn:#f5a524;
  --dot:#c9c6f2;
  --dot-core:#2e2b6a;
  --link:#3fd1a0;
}
*{box-sizing:border-box;margin:0;padding:0}
html,body{width:1200px;height:716px;overflow:hidden;background:var(--page)}
body{font-family:"Poppins",sans-serif;color:var(--text);position:relative}
.board{position:absolute;left:7px;top:50px;display:grid;grid-template-columns:repeat(6,193.5px);grid-auto-rows:304px;column-gap:5.2px;row-gap:6px}
.card{position:relative;background:var(--card);overflow:hidden}
.card-head{position:absolute;left:0;top:0;width:100%;height:22px;background:var(--card-head)}
.updated{position:absolute;left:9.5px;top:8.5px;font-size:4px;color:var(--muted)}
.updated b{color:var(--text);font-weight:600}
.delta{position:absolute;right:7px;top:5.5px;height:11px;padding:0 5px;border-radius:6px;font-size:4.6px;font-weight:600;display:flex;align-items:center;gap:2px;color:#fff}
.delta.up{background:var(--up)}.delta.down{background:var(--down)}.delta.warn{background:var(--warn)}
.delta .ok{width:7px;height:7px;border-radius:50%;background:#fff;display:inline-flex;align-items:center;justify-content:center}
.skyline{position:absolute;left:0;top:0;width:100%;height:262.5px}
.skyline i{position:absolute;bottom:0;width:21px;background:var(--ghost)}
.amount{position:absolute;left:0;width:100%;top:29px;text-align:center;font-family:"Oswald",sans-serif;font-weight:500;font-size:15.5px;line-height:21px}
.label{position:absolute;left:0;width:100%;top:50.5px;text-align:center;font-size:7.2px;font-weight:600;color:var(--accent);line-height:10px}
.caption{position:absolute;left:0;width:100%;top:71px;text-align:center;font-size:7.8px;line-height:10px}
.gauge{position:absolute;left:74px;top:88px;width:45.5px;height:174px;background:var(--bar-empty)}
.gauge .unpaid,.gauge .paid{position:absolute;left:0;bottom:0;width:100%}
.gauge .unpaid{height:calc(var(--u)*1%);background:var(--bar-unpaid)}
.gauge .paid{height:calc(var(--p)*1%);background:var(--bar-paid)}
.gauge .tick{position:absolute;left:38.5px;width:4px;height:1.5px;background:var(--accent);bottom:calc(var(--k)*1%)}
.gauge .dot{position:absolute;left:50%;bottom:calc(var(--t)*1%);width:6px;height:6px;margin-left:-3px;margin-bottom:-3px;border-radius:50%;background:var(--dot)}
.gauge .dot::after{content:"";position:absolute;left:2px;top:2px;width:2px;height:2px;border-radius:50%;background:var(--dot-core)}
.scale{position:absolute;left:124px;top:88px;height:174px;width:30px}
.scale span{position:absolute;left:0;font-size:3.4px;color:var(--muted);transform:translateY(50%);white-space:nowrap}
.target{position:absolute;left:19px;width:39px;height:18px;background:#fff;border-radius:2px;color:#1c1a35;text-align:center;top:calc(88px + 174px*(1 - var(--t)/100) - 11px)}
.target small{display:block;font-size:3.8px;line-height:5px;margin-top:2.5px}
.target strong{display:block;font-family:"Oswald",sans-serif;font-weight:500;font-size:6px;line-height:8px}
.link{position:absolute;left:59px;width:35px;height:8px;top:calc(88px + 174px*(1 - var(--t)/100) - 5px)}
.rate{position:absolute;left:147px;top:139.5px;width:37px;height:13.5px;border-radius:7px;background:#fff;color:#1c1a35;font-size:3.9px;display:flex;align-items:center;justify-content:center;gap:1.5px}
.rate b{font-weight:600;font-size:4.4px}
.card-foot{position:absolute;left:0;top:262.5px;width:100%;height:41.5px;background:var(--card-foot)}
.chip{position:absolute;top:15.5px;height:12.5px;background:var(--chip);border:.5px solid var(--chip-line);border-radius:1.5px;display:flex;align-items:center;gap:2.5px;padding:0 4px;font-size:3.9px;color:var(--muted);white-space:nowrap}
.chip b{font-family:"Oswald",sans-serif;font-weight:500;font-size:4.6px;color:#fff}
.chip .sw{width:5px;height:5px;border-radius:1px}
.chip.unpaid{left:27px;width:53.5px}.chip.unpaid .sw{background:var(--bar-unpaid)}
.chip.paid{left:86px;width:47px}.chip.paid .sw{background:var(--bar-paid)}
.chip.trend{left:138.5px;width:20.5px;justify-content:center;padding:0}
</style>
</head>
<body>
<svg width="0" height="0" style="position:absolute">
  <defs>
    <symbol id="curve" viewBox="0 0 35 8"><path d="M1 5 C6 7 9 7 13 5 S22 2 27 3 S31 4 34 4" fill="none" stroke="var(--link)" stroke-width=".6" stroke-dasharray="1 .8"/><path d="M1 5 l2 -1.2 M1 5 l2 1" stroke="var(--link)" stroke-width=".5"/></symbol>
    <symbol id="bars" viewBox="0 0 12 10"><g fill="none" stroke="var(--accent)" stroke-width=".7"><path d="M1 9.5h10"/><rect x="1.8" y="6" width="1.6" height="3.5"/><rect x="4.4" y="4.5" width="1.6" height="5"/><rect x="7" y="5.5" width="1.6" height="4"/><rect x="9.4" y="3" width="1.6" height="6.5"/><path d="M1.5 4.5 L4 2.5 L6.5 3.6 L10.8 .8"/></g></symbol>
  </defs>
</svg>

<main class="board">

<!-- card template repeated -->
<section class="card" style="--p:29;--u:40;--t:35;--k:28">
  <div class="skyline"><i style="left:1px;height:44px"></i><i style="left:22px;height:79px"></i><i style="left:53px;height:112px"></i><i style="left:140px;height:65px"></i><i style="left:171px;height:105px"></i></div>
  <header class="card-head"><p class="updated">Updated : <b>Jul 20</b></p><span class="delta up">$ 217.75 K ↑</span></header>
  <p class="amount">$ 1.67 M</p><h2 class="label">FOUNDATION CONTRIBUTIONS</h2><p class="caption">Budget</p>
  <div class="gauge"><div class="unpaid"></div><div class="paid"></div><span class="tick"></span><span class="dot"></span></div>
  <div class="scale"><span style="bottom:171px">$ 4.51 M</span><span style="bottom:155px">90%</span><span style="bottom:138px">80%</span><span style="bottom:121px">70%</span><span style="bottom:104px">60%</span><span style="bottom:87.5px">50%</span><span style="bottom:70.5px">40%</span><span style="bottom:54px">30%</span><span style="bottom:37px">20%</span><span style="bottom:20px">10%</span><span style="bottom:3.5px">0%</span></div>
  <div class="target"><small>YTD Target</small><strong>$ 1.45 M</strong></div>
  <svg class="link"><use href="#curve"/></svg>
  <p class="rate">Sub Rate <b>77%</b></p>
  <footer class="card-foot"><span class="chip unpaid"><i class="sw"></i>Unpaid <b>$ 417.35 K</b></span><span class="chip paid"><i class="sw"></i>Paid <b>$ 1.25 M</b></span><span class="chip trend"><svg width="11" height="9"><use href="#bars"/></svg></span></footer>
</section>

<section class="card" style="--p:31;--u:49;--t:44;--k:32">
  <div class="skyline"><i style="left:1px;height:44px"></i><i style="left:22px;height:79px"></i><i style="left:53px;height:112px"></i><i style="left:140px;height:65px"></i><i style="left:171px;height:105px"></i></div>
  <header class="card-head"><p class="updated">Updated : <b>Jul 20</b></p><span class="delta up">$ 67.37 K ↑</span></header>
  <p class="amount">$ 815.92 K</p><h2 class="label">INDIVIDUAL CONTRIBUTIONS</h2><p class="caption">Budget</p>
  <div class="gauge"><div class="unpaid"></div><div class="paid"></div><span class="tick"></span><span class="dot"></span></div>
  <div class="scale"><span style="bottom:171px">$ 1.74 M</span><span style="bottom:155px">90%</span><span style="bottom:138px">80%</span><span style="bottom:121px">70%</span><span style="bottom:104px">60%</span><span style="bottom:87.5px">50%</span><span style="bottom:70.5px">40%</span><span style="bottom:54px">30%</span><span style="bottom:37px">20%</span><span style="bottom:20px">10%</span><span style="bottom:3.5px">0%</span></div>
  <div class="target"><small>YTD Target</small><strong>$ 748.55 K</strong></div>
  <svg class="link"><use href="#curve"/></svg>
  <p class="rate">Sub Rate <b>92%</b></p>
  <footer class="card-foot"><span class="chip unpaid"><i class="sw"></i>Unpaid <b>$ 285.57 K</b></span><span class="chip paid"><i class="sw"></i>Paid <b>$ 530.35 K</b></span><span class="chip trend"><svg width="11" height="9"><use href="#bars"/></svg></span></footer>
</section>

<section class="card" style="--p:40;--u:43;--t:48;--k:31">
  <div class="skyline"><i style="left:1px;height:44px"></i><i style="left:22px;height:79px"></i><i style="left:53px;height:112px"></i><i style="left:140px;height:65px"></i><i style="left:171px;height:105px"></i></div>
  <header class="card-head"><p class="updated">Updated : <b>Jul 20</b></p><span class="delta down">$ -86.28 K ↓</span></header>
  <p class="amount">$ 698.08 K</p><h2 class="label">BUSINESS CONTRIBUTIONS</h2><p class="caption">Budget</p>
  <div class="gauge"><div class="unpaid"></div><div class="paid"></div><span class="tick"></span><span class="dot"></span></div>
  <div class="scale"><span style="bottom:171px">$ 1.66 M</span><span style="bottom:155px">90%</span><span style="bottom:138px">80%</span><span style="bottom:121px">70%</span><span style="bottom:104px">60%</span><span style="bottom:87.5px">50%</span><span style="bottom:70.5px">40%</span><span style="bottom:54px">30%</span><span style="bottom:37px">20%</span><span style="bottom:20px">10%</span><span style="bottom:3.5px">0%</span></div>
  <div class="target"><small>YTD Target</small><strong>$ 784.36 K</strong></div>
  <svg class="link"><use href="#curve"/></svg>
  <p class="rate">Sub Rate <b>93%</b></p>
  <footer class="card-foot"><span class="chip unpaid"><i class="sw"></i>Unpaid <b>$ 55.85 K</b></span><span class="chip paid"><i class="sw"></i>Paid <b>$ 642.23 K</b></span><span class="chip trend"><svg width="11" height="9"><use href="#bars"/></svg></span></footer>
</section>

<section class="card" style="--p:50;--u:60;--t:65;--k:21">
  <div class="skyline"><i style="left:1px;height:44px"></i><i style="left:22px;height:79px"></i><i style="left:53px;height:112px"></i><i style="left:140px;height:65px"></i><i style="left:171px;height:105px"></i></div>
  <header class="card-head"><p class="updated">Updated : <b>Jul 20</b></p><span class="delta down">$ -39.68 K ↓</span></header>
  <p class="amount">$ 456.34 K</p><h2 class="label">GRANTS FROM NATIONAL</h2><p class="caption">Budget</p>
  <div class="gauge"><div class="unpaid"></div><div class="paid"></div><span class="tick"></span><span class="dot"></span></div>
  <div class="scale"><span style="bottom:171px">$ 760.57 K</span><span style="bottom:155px">90%</span><span style="bottom:138px">80%</span><span style="bottom:121px">70%</span><span style="bottom:104px">60%</span><span style="bottom:87.5px">50%</span><span style="bottom:70.5px">40%</span><span style="bottom:54px">30%</span><span style="bottom:37px">20%</span><span style="bottom:20px">10%</span><span style="bottom:3.5px">0%</span></div>
  <div class="target"><small>YTD Target</small><strong>$ 496.02 K</strong></div>
  <svg class="link"><use href="#curve"/></svg>
  <p class="rate">Sub Rate <b>76%</b></p>
  <footer class="card-foot"><span class="chip unpaid"><i class="sw"></i>Unpaid <b>$ 63.89 K</b></span><span class="chip paid"><i class="sw"></i>Paid <b>$ 392.45 K</b></span><span class="chip trend"><svg width="11" height="9"><use href="#bars"/></svg></span></footer>
</section>

<section class="card" style="--p:59;--u:76;--t:73;--k:30">
  <div class="skyline"><i style="left:1px;height:44px"></i><i style="left:22px;height:79px"></i><i style="left:53px;height:112px"></i><i style="left:140px;height:65px"></i><i style="left:171px;height:105px"></i></div>
  <header class="card-head"><p class="updated">Updated : <b>Jul 20</b></p><span class="delta up">$ 10.07 K ↑</span></header>
  <p class="amount">$ 345.73 K</p><h2 class="label">SPECIAL EVENTS</h2><p class="caption">Budget</p>
  <div class="gauge"><div class="unpaid"></div><div class="paid"></div><span class="tick"></span><span class="dot"></span></div>
  <div class="scale"><span style="bottom:171px">$ 460.97 K</span><span style="bottom:155px">90%</span><span style="bottom:138px">80%</span><span style="bottom:121px">70%</span><span style="bottom:104px">60%</span><span style="bottom:87.5px">50%</span><span style="bottom:70.5px">40%</span><span style="bottom:54px">30%</span><span style="bottom:37px">20%</span><span style="bottom:20px">10%</span><span style="bottom:3.5px">0%</span></div>
  <div class="target"><small>YTD Target</small><strong>$ 335.66 K</strong></div>
  <svg class="link"><use href="#curve"/></svg>
  <p class="rate">Sub Rate <b>90%</b></p>
  <footer class="card-foot"><span class="chip unpaid"><i class="sw"></i>Unpaid <b>$ 72.60 K</b></span><span class="chip paid"><i class="sw"></i>Paid <b>$ 273.12 K</b></span><span class="chip trend"><svg width="11" height="9"><use href="#bars"/></svg></span></footer>
</section>

<section class="card" style="--p:31;--u:34;--t:20;--k:33">
  <div class="skyline"><i style="left:1px;height:44px"></i><i style="left:22px;height:79px"></i><i style="left:53px;height:112px"></i><i style="left:140px;height:65px"></i><i style="left:171px;height:105px"></i></div>
  <header class="card-head"><p class="updated">Updated : <b>Jul 20</b></p><span class="delta down">$ -89.12 K ↓</span></header>
  <p class="amount">$ 32.96 K</p><h2 class="label">OTHER INCOME</h2><p class="caption">Budget</p>
  <div class="gauge"><div class="unpaid"></div><div class="paid"></div><span class="tick"></span><span class="dot"></span></div>
  <div class="scale"><span style="bottom:171px">$ 103.01 K</span><span style="bottom:155px">90%</span><span style="bottom:138px">80%</span><span style="bottom:121px">70%</span><span style="bottom:104px">60%</span><span style="bottom:87.5px">50%</span><span style="bottom:70.5px">40%</span><span style="bottom:54px">30%</span><span style="bottom:37px">20%</span><span style="bottom:20px">10%</span><span style="bottom:3.5px">0%</span></div>
  <div class="target"><small>YTD Target</small><strong>$ 335.66 K</strong></div>
  <svg class="link"><use href="#curve"/></svg>
  <p class="rate">Sub Rate <b>83%</b></p>
  <footer class="card-foot"><span class="chip unpaid"><i class="sw"></i>Unpaid <b>$ 1.65 K</b></span><span class="chip paid"><i class="sw"></i>Paid <b>$ 31.32 K</b></span><span class="chip trend"><svg width="11" height="9"><use href="#bars"/></svg></span></footer>
</section>

<section class="card" style="--p:40;--u:41;--t:52;--k:28">
  <div class="skyline"><i style="left:1px;height:44px"></i><i style="left:22px;height:79px"></i><i style="left:53px;height:112px"></i><i style="left:140px;height:65px"></i><i style="left:171px;height:105px"></i></div>
  <header class="card-head"><p class="updated">Updated : <b>Jul 20</b></p><span class="delta down">$ 12.12 K ↓</span></header>
  <p class="amount">$ 36.35 K</p><h2 class="label">NET ASSETS RELEASED FROM....</h2><p class="caption">Budget</p>
  <div class="gauge"><div class="unpaid"></div><div class="paid"></div><span class="tick"></span><span class="dot"></span></div>
  <div class="scale"><span style="bottom:171px">$ 95.66 K</span><span style="bottom:155px">90%</span><span style="bottom:138px">80%</span><span style="bottom:121px">70%</span><span style="bottom:104px">60%</span><span style="bottom:87.5px">50%</span><span style="bottom:70.5px">40%</span><span style="bottom:54px">30%</span><span style="bottom:37px">20%</span><span style="bottom:20px">10%</span><span style="bottom:3.5px">0%</span></div>
  <div class="target"><small>YTD Target</small><strong>$ 48.47 K</strong></div>
  <svg class="link"><use href="#curve"/></svg>
  <p class="rate">Sub Rate <b>76%</b></p>
  <footer class="card-foot"><span class="chip unpaid"><i class="sw"></i>Unpaid <b>$ 0.00 K</b></span><span class="chip paid"><i class="sw"></i>Paid <b>$ 36.35 K</b></span><span class="chip trend"><svg width="11" height="9"><use href="#bars"/></svg></span></footer>
</section>

<section class="card" style="--p:31;--u:45;--t:44;--k:25">
  <div class="skyline"><i style="left:1px;height:44px"></i><i style="left:22px;height:79px"></i><i style="left:53px;height:112px"></i><i style="left:140px;height:65px"></i><i style="left:171px;height:105px"></i></div>
  <header class="card-head"><p class="updated">Updated : <b>Jul 20</b></p><span class="delta up">$ 67.98 K ↑</span></header>
  <p class="amount">$ 4.05 M</p><h2 class="label">TOTAL RECEIPTS</h2><p class="caption">Budget</p>
  <div class="gauge"><div class="unpaid"></div><div class="paid"></div><span class="tick"></span><span class="dot"></span></div>
  <div class="scale"><span style="bottom:171px">$ 9.33 M</span><span style="bottom:155px">90%</span><span style="bottom:138px">80%</span><span style="bottom:121px">70%</span><span style="bottom:104px">60%</span><span style="bottom:87.5px">50%</span><span style="bottom:70.5px">40%</span><span style="bottom:54px">30%</span><span style="bottom:37px">20%</span><span style="bottom:20px">10%</span><span style="bottom:3.5px">0%</span></div>
  <div class="target"><small>YTD Target</small><strong>$ 3.99 M</strong></div>
  <svg class="link"><use href="#curve"/></svg>
  <p class="rate">Sub Rate <b>93%</b></p>
  <footer class="card-foot"><span class="chip unpaid"><i class="sw"></i>Unpaid <b>$ 896.90 K</b></span><span class="chip paid"><i class="sw"></i>Paid <b>$ 3.16 M</b></span><span class="chip trend"><svg width="11" height="9"><use href="#bars"/></svg></span></footer>
</section>

<section class="card" style="--p:37;--u:39;--t:41;--k:27">
  <div class="skyline"><i style="left:1px;height:44px"></i><i style="left:22px;height:79px"></i><i style="left:53px;height:112px"></i><i style="left:140px;height:65px"></i><i style="left:171px;height:105px"></i></div>
  <header class="card-head"><p class="updated">Updated : <b>Jul 20</b></p><span class="delta up">$ 14.02 K ↓</span></header>
  <p class="amount">$ 698.08 K</p><h2 class="label">SALARIES AND WAGES</h2><p class="caption">Budget</p>
  <div class="gauge"><div class="unpaid"></div><div class="paid"></div><span class="tick"></span><span class="dot"></span></div>
  <div class="scale"><span style="bottom:171px">$ 1.96 M</span><span style="bottom:155px">90%</span><span style="bottom:138px">80%</span><span style="bottom:121px">70%</span><span style="bottom:104px">60%</span><span style="bottom:87.5px">50%</span><span style="bottom:70.5px">40%</span><span style="bottom:54px">30%</span><span style="bottom:37px">20%</span><span style="bottom:20px">10%</span><span style="bottom:3.5px">0%</span></div>
  <div class="target"><small>YTD Target</small><strong>$ 700.97 K</strong></div>
  <svg class="link"><use href="#curve"/></svg>
  <p class="rate">Sub Rate <b>79%</b></p>
  <footer class="card-foot"><span class="chip unpaid"><i class="sw"></i>Unpaid <b>$ 34.35 K</b></span><span class="chip paid"><i class="sw"></i>Paid <b>$ 652.20 K</b></span><span class="chip trend"><svg width="11" height="9"><use href="#bars"/></svg></span></footer>
</section>

<section class="card" style="--p:36;--u:38;--t:39;--k:21">
  <div class="skyline"><i style="left:1px;height:44px"></i><i style="left:22px;height:79px"></i><i style="left:53px;height:112px"></i><i style="left:140px;height:65px"></i><i style="left:171px;height:105px"></i></div>
  <header class="card-head"><p class="updated">Updated : <b>Jul 20</b></p><span class="delta warn">$ 802.00 K ↓</span></header>
  <p class="amount">$ 39.28 K</p><h2 class="label">PAYROLL TAXES</h2><p class="caption">Budget</p>
  <div class="gauge"><div class="unpaid"></div><div class="paid"></div><span class="tick"></span><span class="dot"></span></div>
  <div class="scale"><span style="bottom:171px">$ 112.23 K</span><span style="bottom:155px">90%</span><span style="bottom:138px">80%</span><span style="bottom:121px">70%</span><span style="bottom:104px">60%</span><span style="bottom:87.5px">50%</span><span style="bottom:70.5px">40%</span><span style="bottom:54px">30%</span><span style="bottom:37px">20%</span><span style="bottom:20px">10%</span><span style="bottom:3.5px">0%</span></div>
  <div class="target"><small>YTD Target</small><strong>$ 40.08 K</strong></div>
  <svg class="link"><use href="#curve"/></svg>
  <p class="rate">Sub Rate <b>89%</b></p>
  <footer class="card-foot"><span class="chip unpaid"><i class="sw"></i>Unpaid <b>$ 1.96 K</b></span><span class="chip paid"><i class="sw"></i>Paid <b>$ 37.32 K</b></span><span class="chip trend"><svg width="11" height="9"><use href="#bars"/></svg></span></footer>
</section>

<section class="card" style="--p:36;--u:37;--t:46;--k:31">
  <div class="skyline"><i style="left:1px;height:44px"></i><i style="left:22px;height:79px"></i><i style="left:53px;height:112px"></i><i style="left:140px;height:65px"></i><i style="left:171px;height:105px"></i></div>
  <header class="card-head"><p class="updated">Updated : <b>Jul 20</b></p><span class="delta up">$ 73.36 K ↑ <span class="ok"><svg width="5" height="5" viewBox="0 0 10 10"><path d="M2 5.2l2 2 4-4.4" fill="none" stroke="var(--up)" stroke-width="1.8"/></svg></span></span></header>
  <p class="amount">$ 260.10 K</p><h2 class="label">BENEFITS</h2><p class="caption">Budget</p>
  <div class="gauge"><div class="unpaid"></div><div class="paid"></div><span class="tick"></span><span class="dot"></span></div>
  <div class="scale"><span style="bottom:171px">$ 743.15 K</span><span style="bottom:155px">90%</span><span style="bottom:138px">80%</span><span style="bottom:121px">70%</span><span style="bottom:104px">60%</span><span style="bottom:87.5px">50%</span><span style="bottom:70.5px">40%</span><span style="bottom:54px">30%</span><span style="bottom:37px">20%</span><span style="bottom:20px">10%</span><span style="bottom:3.5px">0%</span></div>
  <div class="target"><small>YTD Target</small><strong>$ 335.66 K</strong></div>
  <svg class="link"><use href="#curve"/></svg>
  <p class="rate">Sub Rate <b>78%</b></p>
  <footer class="card-foot"><span class="chip unpaid"><i class="sw"></i>Unpaid <b>$ 5.20 K</b></span><span class="chip paid"><i class="sw"></i>Paid <b>$ 254.90 K</b></span><span class="chip trend"><svg width="11" height="9"><use href="#bars"/></svg></span></footer>
</section>

<section class="card" style="--p:31;--u:35;--t:40;--k:31">
  <div class="skyline"><i style="left:1px;height:44px"></i><i style="left:22px;height:79px"></i><i style="left:53px;height:112px"></i><i style="left:140px;height:65px"></i><i style="left:171px;height:105px"></i></div>
  <header class="card-head"><p class="updated">Updated : <b>Jul 20</b></p><span class="delta up">$ 13.55 K ↓</span></header>
  <p class="amount">$ 83.21 K</p><h2 class="label">OTHER EXPENSES</h2><p class="caption">Budget</p>
  <div class="gauge"><div class="unpaid"></div><div class="paid"></div><span class="tick"></span><span class="dot"></span></div>
  <div class="scale"><span style="bottom:171px">$ 252.15 K</span><span style="bottom:155px">90%</span><span style="bottom:138px">80%</span><span style="bottom:121px">70%</span><span style="bottom:104px">60%</span><span style="bottom:87.5px">50%</span><span style="bottom:70.5px">40%</span><span style="bottom:54px">30%</span><span style="bottom:37px">20%</span><span style="bottom:20px">10%</span><span style="bottom:3.5px">0%</span></div>
  <div class="target"><small>YTD Target</small><strong>$ 335.66 K</strong></div>
  <svg class="link"><use href="#curve"/></svg>
  <p class="rate">Sub Rate <b>78%</b></p>
  <footer class="card-foot"><span class="chip unpaid"><i class="sw"></i>Unpaid <b>$ 12.48 K</b></span><span class="chip paid"><i class="sw"></i>Paid <b>$ 70.73 K</b></span><span class="chip trend"><svg width="11" height="9"><use href="#bars"/></svg></span></footer>
</section>

</main>
</body>
</html>
```